Build a Web page - Dovin Pratchell Homes, LLC - a custom home builder

We are a custom home builder in Wisconsin. Need a basic web page with a home page, About Us, Contact info, Gallery, and Testimonials page. Gallery will probably have sub-pages and each will have about ten pictures or less. I already own the domain and have web hosting through Wix, I just need the site built. Once the page is built I should be able to do the upkeep on it myself. If I need to add pictures or whatever.
Updates

Project Deadline Extended
Reason: I am still looking through designs and will select soon - thank you!

Target Market(s)

Gen X and Millennials who are looking to build a home. Custom built homes - not generic spec homes.

Industry/Entity Type

Home Builder

Number of Pages Required

5+ page

Font styles to use
Sans Serif

Colors
ffffff
ec1f27
000000
9d9d9d

Requirements
Must have
• I have no idea if I want coded or in coded. I'm not sure of the difference and why I would want one over the other.
Nice to have
• We like the following colors - red, black, gray, white.
Should not have
• not a big fan of clip art like hammers, tape measures, etc. Must look professional.

```html
<!DOCTYPE html>
<html lang="en">
<head>
<meta charset="utf-8">
<title>Dovin Pratchell Homes, LLC</title>
<link href="https://fonts.googleapis.com/css2?family=Montserrat:ital,wght@0,400;0,500;0,600;0,700;1,400&family=Poppins:wght@300;400;500;600&family=Great+Vibes&display=swap" rel="stylesheet">
<style>
:root{
  --red:#a1181d;
  --red-bright:#c8161d;
  --black:#000;
  --ink:#1d1d1d;
  --text:#333;
  --grey:#9d9d9d;
  --grey-light:#e6e6e6;
  --grey-band:#dedede;
  --white:#fff;
  --footer:#2b2b2b;
}
*{margin:0;padding:0;box-sizing:border-box}
html,body{width:1200px;height:2885px;overflow:hidden}
body{font-family:'Montserrat',sans-serif;color:var(--text);background:var(--white);position:relative}
.section{position:absolute;left:0;width:1200px}
.btn{position:absolute;background:var(--black);color:var(--white);font:700 11px 'Montserrat',sans-serif;letter-spacing:.5px;display:flex;align-items:center;justify-content:center;text-transform:uppercase}

/* header */
.site-header{top:0;height:96px;border-bottom:3px solid var(--red);box-shadow:0 2px 0 #d7a0a2}
.brand{position:absolute;left:73px;top:18px;display:flex;align-items:center;gap:8px}
.brand-mark{width:18px;height:18px;background:var(--red);flex:none}
.brand-name{font:700 14px 'Montserrat',sans-serif;color:var(--red);line-height:1.15;width:100px}
.main-nav{position:absolute;left:346px;top:38px;display:flex}
.main-nav a{font:600 14px 'Montserrat',sans-serif;color:var(--ink);text-decoration:none;text-transform:uppercase;margin-right:40px}
.call-box{position:absolute;right:0;top:0;width:306px;height:92px;background:#ececec;clip-path:polygon(8% 0,100% 0,100% 100%,0 100%)}
.call-icon{position:absolute;left:28px;top:27px}
.call-text{position:absolute;left:80px;top:24px;color:var(--black)}
.call-text span{display:block;font:500 16px 'Montserrat',sans-serif}
.call-text strong{display:block;font:700 22px 'Montserrat',sans-serif;line-height:1.1}

/* hero */
.hero{top:96px;height:589px;background:linear-gradient(180deg,#6e93c4 0%,#a9c0dc 28%,#8a8c84 45%,#6b6f5c 60%,#4f7a2f 78%,#6d9440 100%)}
.hero-title{position:absolute;left:0;width:1200px;top:215px;text-align:center;color:var(--white);font-family:'Great Vibes',cursive}
.hero-title small{display:block;font-size:40px;line-height:1}
.hero-title span{display:block;font-size:82px;line-height:1}
.hero-rule{position:absolute;left:425px;top:341px;width:370px;height:3px;background:var(--white)}
.hero-arrow{position:absolute;top:277px}

/* welcome */
.welcome{top:685px;height:340px;text-align:center}
.welcome h2{position:absolute;top:40px;width:100%;font:400 26px 'Poppins',sans-serif;color:var(--black)}
.welcome h1{position:absolute;top:70px;width:100%;font:600 33px 'Montserrat',sans-serif;color:var(--red)}
.title-rule{position:absolute;height:3px;background:var(--red)}
.welcome p{position:absolute;left:84px;width:1032px;top:142px;font-size:14px;line-height:25px}

/* gallery */
.gallery{top:1025px;height:306px;background:var(--red)}
.gallery h3{position:absolute;left:73px;top:42px;font:500 27px 'Poppins',sans-serif;color:var(--white)}
.gallery .btn{left:1015px;top:46px;width:110px;height:30px}
.gallery-item{position:absolute;top:104px;width:252px;height:154px;border:3px solid var(--white)}
.g1{left:73px;background:linear-gradient(135deg,#b99779,#7b4b3a 60%,#9c3b34)}
.g2{left:340px;background:linear-gradient(135deg,#d9d4c6,#a88a55 55%,#6f6258)}
.g3{left:608px;background:linear-gradient(135deg,#f2f2f0,#cfcfcf 55%,#7a7670)}
.g4{left:875px;background:linear-gradient(135deg,#efeeea,#b07142 55%,#6f3b22)}

/* testimonials */
.testimonials{top:1331px;height:471px}
.section-title{position:absolute;width:100%;text-align:center;font:400 26px 'Poppins',sans-serif;color:var(--black)}
.testimonials .section-title{top:37px}
.title-line{position:absolute;left:450px;top:83px;width:300px;height:1px;background:#ddd}
.testimonial{position:absolute;top:115px;width:333px;height:252px;background:var(--grey-light);padding:20px 22px 0 52px}
.quote-mark{position:absolute;left:18px;top:14px;font:700 50px Georgia,serif;color:#c2c2c2;line-height:1}
.testimonial p{font:italic 400 14px 'Montserrat',sans-serif;line-height:24px;color:#444}
.author{position:absolute;left:52px;top:182px;display:flex;align-items:center;gap:14px;font:600 13.5px 'Montserrat',sans-serif;color:var(--ink)}
.avatar{width:52px;height:52px;border-radius:50%;background:linear-gradient(180deg,#9fb0ba,#6c7c86);border:2px solid var(--white)}
.t1{left:73px}.t2{left:433px}.t3{left:793px}
.testimonials .btn{left:546px;top:396px;width:108px;height:31px}

/* process */
.process{top:1802px;height:285px;background:linear-gradient(180deg,#3a2a22,#4e382b 50%,#2e231d);text-align:center;color:var(--white)}
.process h3{position:absolute;top:80px;width:100%;font:400 33px 'Poppins',sans-serif}
.process p{position:absolute;top:134px;width:100%;font:300 26px 'Poppins',sans-serif;line-height:33px}

/* method */
.method{top:2087px;height:519px}
.method-heading{position:absolute;top:38px;left:73px;width:1052px;height:34px}
.method-heading .band{position:absolute;top:11px;height:16px;background:var(--grey-band)}
.method-heading h3{position:absolute;left:0;width:100%;text-align:center;font:500 26px 'Poppins',sans-serif;color:var(--black)}
.method-frame{position:absolute;left:88px;top:101px;width:512px;height:365px;background:var(--grey-band)}
.method-photo{position:absolute;left:73px;top:112px;width:517px;height:355px;background:linear-gradient(135deg,#f0ebe1 0%,#8e5a36 35%,#5c3320 65%,#b79f82 100%)}
.method-copy{position:absolute;left:613px;top:108px;width:516px;font-size:14px;line-height:24px}
.features{position:absolute;left:613px;top:294px;list-style:none}
.features li{font-size:14px;line-height:31.5px;display:flex;align-items:center;gap:10px}
.method .btn{left:613px;top:444px;width:110px;height:31px}

/* footer */
.site-footer{top:2606px;height:279px;background:var(--footer);color:#bdbdbd}
.footer-brand{position:absolute;left:73px;top:40px;width:96px;height:88px;background:var(--white);display:flex;align-items:center;justify-content:center;gap:6px;padding:6px}
.footer-brand .brand-mark{width:12px;height:12px}
.footer-brand .brand-name{font-size:11px;width:auto}
.footer-col{position:absolute;top:44px}
.footer-col h4{font:600 16px 'Montserrat',sans-serif;color:var(--white);margin-bottom:14px}
.footer-col li{list-style:none;font-size:13.5px;line-height:28px}
.contact-list li{line-height:22px}
.contact-list .gap{margin-top:14px}
.social li{display:flex;align-items:center;gap:10px;line-height:34px}
.social .dot{width:22px;height:22px;border-radius:50%;background:var(--white)}
.newsletter p{width:345px;font-size:12.5px;line-height:22px;margin-top:-2px}
.subscribe{position:absolute;left:0;top:100px;display:flex}
.subscribe span{width:231px;height:35px;background:var(--white);color:#555;font-size:12.5px;display:flex;align-items:center;padding-left:12px}
.subscribe b{width:100px;height:35px;background:var(--red-bright);color:var(--white);font:600 15px 'Montserrat',sans-serif;display:flex;align-items:center;justify-content:center}
.copyright{position:absolute;top:244px;width:100%;text-align:center;font-size:12.5px}
</style>
</head>
<body>

<header class="section site-header">
  <div class="brand"><span class="brand-mark"></span><span class="brand-name">Dovin Pratchell Homes</span></div>
  <nav class="main-nav">
    <a href="#">Home</a><a href="#">About Us</a><a href="#">Gallery</a><a href="#">Testimonials</a><a href="#">Contact Us</a>
  </nav>
  <div class="call-box">
    <svg class="call-icon" width="38" height="38" viewBox="0 0 38 38"><circle cx="19" cy="19" r="19" fill="#6a6a6a"/><path d="M13 11c1-1 2-1 3 0l2 3c.6 1 .3 1.7-.4 2.4l-1 1c1 2 3 4 5 5l1-1c.7-.7 1.4-1 2.4-.4l3 2c1 1 1 2 0 3l-1.5 1.5c-4 2-15-9-13-13z" fill="#fff"/></svg>
    <div class="call-text"><span>Call Us Today!</span><strong>100-000-0000</strong></div>
  </div>
</header>

<section class="section hero" role="img" aria-label="Photo of a two-storey house with stone garage front, green lawn and blue sky">
  <div class="hero-title"><small>You'll Love Your</small><span>Dovin Pratchell Homes</span></div>
  <div class="hero-rule"></div>
  <svg class="hero-arrow" style="left:28px" width="36" height="36" viewBox="0 0 36 36"><circle cx="18" cy="18" r="16" fill="none" stroke="#fff" stroke-width="2"/><path d="M21 10l-8 8 8 8" fill="none" stroke="#fff" stroke-width="2.5"/></svg>
  <svg class="hero-arrow" style="left:1135px" width="36" height="36" viewBox="0 0 36 36"><circle cx="18" cy="18" r="16" fill="none" stroke="#fff" stroke-width="2"/><path d="M15 10l8 8-8 8" fill="none" stroke="#fff" stroke-width="2.5"/></svg>
</section>

<section class="section welcome">
  <h2>Welcome to</h2>
  <h1>Dovin Pratchell Homes, LLC</h1>
  <div class="title-rule" style="left:573px;top:120px;width:54px"></div>
  <p>Lorem ipsum dolor sit amet, consectetur adipiscing elit, sed do eiusmod tempor incididunt ut labore et dolore magna aliqua. Ut enim ad minim veniam, quis nostrud exercitation ullamco laboris nisi ut aliquip ex ea commodo consequat. Duis aute irure dolor in reprehenderit in voluptate velit esse cillum dolore eu fugiat nulla pariatur. Excepteur sint occaecat cupidatat non proident, sunt in culpa qui officia deserunt mollit anim id est laborum.</p>
  <span class="btn" style="left:546px;top:263px;width:108px;height:31px">Read More</span>
</section>

<section class="section gallery">
  <h3>Our Gallery</h3>
  <span class="btn">View More</span>
  <div class="gallery-item g1" role="img" aria-label="Living room with fireplace and red sofas"></div>
  <div class="gallery-item g2" role="img" aria-label="Bathroom with wood vanity and mirror"></div>
  <div class="gallery-item g3" role="img" aria-label="White bathroom vanity with mounted television"></div>
  <div class="gallery-item g4" role="img" aria-label="Wooden staircase in a bright hallway"></div>
</section>

<section class="section testimonials">
  <h3 class="section-title">What Our Clients Says</h3>
  <div class="title-line"></div>
  <div class="title-rule" style="left:588px;top:82px;width:24px"></div>
  <article class="testimonial t1"><span class="quote-mark">&ldquo;</span><p>Lorem ipsum dolor sit amet, consectetur adipiscing elit, sed do eiusmod tempor incididunt ut labore et dolore magna aliqua. Ut enim ad minim veniam, quis nostrud exercitation.</p><div class="author"><span class="avatar" role="img" aria-label="Client portrait"></span>Delwyn Marsh</div></article>
  <article class="testimonial t2"><span class="quote-mark">&ldquo;</span><p>Lorem ipsum dolor sit amet, consectetur adipiscing elit, sed do eiusmod tempor incididunt ut labore et dolore magna aliqua. Ut enim ad minim veniam, quis nostrud exercitation.</p><div class="author"><span class="avatar" role="img" aria-label="Client portrait"></span>Delwyn Marsh</div></article>
  <article class="testimonial t3"><span class="quote-mark">&ldquo;</span><p>Lorem ipsum dolor sit amet, consectetur adipiscing elit, sed do eiusmod tempor incididunt ut labore et dolore magna aliqua. Ut enim ad minim veniam, quis nostrud exercitation.</p><div class="author"><span class="avatar" role="img" aria-label="Client portrait"></span>Delwyn Marsh</div></article>
  <span class="btn">Read More</span>
</section>

<section class="section process" role="img" aria-label="Darkened photo of a kitchen with wood cabinets">
  <h3>Our Process is Simple</h3>
  <p>Listen to our client's needs, identify every detail in the building process<br>and accept only the highest quality</p>
</section>

<section class="section method">
  <div class="method-heading">
    <div class="band" style="left:0;width:205px"></div>
    <div class="band" style="left:847px;width:205px"></div>
    <h3>Our Innovative Custom Home Building Method</h3>
  </div>
  <div class="method-frame"></div>
  <div class="method-photo" role="img" aria-label="Photo of a kitchen with cherry cabinets, island and pendant lights"></div>
  <p class="method-copy">Sed ut perspiciatis unde omnis iste natus error sit voluptatem accusantium doloremque laudantium, totam rem aperiam, eaque ipsa quae ab illo inventore veritatis et quasi architecto beatae vitae dicta sunt explicabo. Nemo enim ipsam voluptatem quia voluptas sit aspernatur aut odit aut fugit, sed quia consequuntur magni dolores eos qui ratione voluptatem sequi nesciunt. Neque porro quisquam est, qui dolorem ipsum quia dolor sit amet, consectetur,</p>
  <ul class="features">
    <li><svg width="14" height="14" viewBox="0 0 14 14"><circle cx="7" cy="7" r="6" fill="none" stroke="#555"/><path d="M6 4.5L8.5 7 6 9.5" fill="none" stroke="#555"/></svg>Controlled indoor construction</li>
    <li><svg width="14" height="14" viewBox="0 0 14 14"><circle cx="7" cy="7" r="6" fill="none" stroke="#555"/><path d="M6 4.5L8.5 7 6 9.5" fill="none" stroke="#555"/></svg>Intelligent craftsmanship</li>
    <li><svg width="14" height="14" viewBox="0 0 14 14"><circle cx="7" cy="7" r="6" fill="none" stroke="#555"/><path d="M6 4.5L8.5 7 6 9.5" fill="none" stroke="#555"/></svg>Innovative technology</li>
    <li><svg width="14" height="14" viewBox="0 0 14 14"><circle cx="7" cy="7" r="6" fill="none" stroke="#555"/><path d="M6 4.5L8.5 7 6 9.5" fill="none" stroke="#555"/></svg>Sustainable design</li>
  </ul>
  <span class="btn">Read More</span>
</section>

<footer class="section site-footer">
  <div class="footer-brand"><span class="brand-mark"></span><span class="brand-name">Dovin Pratchell Homes</span></div>
  <div class="footer-col" style="left:229px"><h4>Quick Links</h4><ul><li>Home</li><li>About Us</li><li>Gallery</li><li>Testimonials</li><li>Contact Us</li></ul></div>
  <div class="footer-col" style="left:381px"><h4>Contact Us</h4><ul class="contact-list"><li>Dovin Pratchell Homes, LLC</li><li>Street Name, 000000</li><li>City Name</li><li class="gap">P: 100-000-0000</li><li class="gap">E: info@dovinpratchell.com</li></ul></div>
  <div class="footer-col social" style="left:613px"><h4>Keep in Touch</h4><ul><li><span class="dot"></span>Neighborly</li><li><span class="dot"></span>Chirpline</li><li><span class="dot"></span>Snapframe</li><li><span class="dot"></span>Workgrid</li></ul></div>
  <div class="footer-col newsletter" style="left:794px"><h4>Get The Subscribe Newsletter</h4><p>Lorem ipsum dolor sit amet, consectetur adipi scing elit, sed do eiusmod tempor incididunt.</p><div class="subscribe"><span>Enter your email address</span><b>Subscribe</b></div></div>
  <p class="copyright">&copy; 2017 Dovin Pratchell Homes, LLC. All Rights Reserved.</p>
</footer>

</body>
</html>
```